Post card

I want an educational customer postcard with our logo, email, and contact number. We are a residential foundation inspection & repair company here in Los Angeles. We provide foundation repair, earthquake retrofitting, and reinforcement.
Our number is 323-555-0148.
Email info@bramblecrestworks.com
Our license number is #2839165

OUR GOAL
Our primary objective is to empower clients with comprehensive knowledge about foundation issues and earthquake retrofitting. By educating them on the potential risks associated with foundation problems and the importance of earthquake retrofitting, we aim to equip homeowners with the necessary information to make informed decisions about safeguarding their properties. Highlighting the benefits of having their houses properly bolted not only enhances structural integrity but also provides peace of mind during seismic events, ensuring the safety and security of their homes and loved ones.

```html
<!DOCTYPE html>
<html lang="en">
<head>
<meta charset="utf-8">
<title>Bramblecrest Works – Postcard</title>
<link href="https://fonts.googleapis.com/css2?family=Open+Sans:wght@300;400;600;700&display=swap" rel="stylesheet">
<style>
  :root {
    --stage: #dcdde0;
    --white: #ffffff;
    --brand-blue: #2f5fb8;
    --panel-deep: #1f48a6;
    --panel-bright: #00a9e8;
    --pale-blue: #8fb8e0;
    --sky: #6fcdf2;
    --red: #d7232d;
    --orange: #f7941d;
    --ink: #333333;
    --address-gray: #f0f0f2;
    --address-edge: #dedfe3;
    --rule: #9a9a9e;
  }
  * { box-sizing: border-box; margin: 0; padding: 0; }
  html, body { width: 1200px; height: 642px; overflow: hidden; }
  body {
    background: var(--stage);
    font-family: "Open Sans", Arial, sans-serif;
    color: var(--ink);
    position: relative;
  }
  .postcard {
    position: absolute;
    top: 122px;
    width: 560px;
    height: 398px;
    background: var(--white);
    overflow: hidden;
  }
  .postcard--front { left: 25px; }
  .postcard--back { left: 615px; }
  .card-shapes { position: absolute; inset: 0; }

  /* Front */
  .brand {
    position: absolute; left: 29px; top: 26px;
    display: flex; align-items: center; gap: 9px;
  }
  .brand-mark { width: 30px; height: 30px; background: var(--brand-blue); flex: none; }
  .brand-name {
    font-weight: 700; font-size: 21px; line-height: 22px;
    color: var(--brand-blue); letter-spacing: 0.4px; text-transform: uppercase;
  }
  .license {
    position: absolute; left: 150px; top: 78px; width: 67px; text-align: right;
    font-size: 7px; font-weight: 700; color: var(--ink);
  }
  .tagline {
    position: absolute; left: 294px; top: 22px;
    font-weight: 300; font-size: 24px; line-height: 27px; color: var(--ink);
  }
  .hero-photo {
    position: absolute; inset: 0;
    clip-path: polygon(229px 87px, 560px 87px, 560px 361px, 368px 361px);
    background: linear-gradient(150deg, #c9d3dc 0%, #e2b273 35%, #e89a2e 50%, #3c3f5e 65%, #a9b2bb 100%);
  }
  .hero-copy {
    position: absolute; left: 26px; top: 178px;
    color: var(--white); text-transform: uppercase; font-size: 16px; line-height: 19.5px;
  }
  .hero-copy .light { font-weight: 400; }
  .hero-copy .strong { font-weight: 700; font-size: 16.5px; }
  .hero-copy .city { font-weight: 700; font-size: 22px; line-height: 26px; color: var(--orange); }
  .phone {
    position: absolute; left: 26px; top: 340px;
    font-weight: 700; font-size: 27px; line-height: 30px; color: var(--red);
  }
  .phone-note { position: absolute; left: 26px; top: 370px; font-size: 12px; }
  .email {
    position: absolute; left: 325px; top: 371px;
    display: flex; align-items: center; gap: 6px; font-size: 14px;
  }

  /* Back */
  .services {
    position: absolute; left: 27px; top: 22px; list-style: none;
    font-size: 14px; line-height: 18.5px; color: var(--brand-blue);
  }
  .services li { display: flex; align-items: center; gap: 6px; }
  .services li::before {
    content: ""; width: 11px; height: 11px; border-radius: 50%;
    background: radial-gradient(circle at 35% 35%, #ff6b6b, var(--red) 70%);
  }
  .goal {
    position: absolute; left: 27px; top: 88px; width: 248px;
    font-size: 9.3px; line-height: 11.1px; text-align: justify;
  }
  .goal p + p { margin-top: 6px; }
  .goal p:last-child { width: 270px; }
  .work-photo {
    position: absolute; inset: 0;
    clip-path: polygon(27px 252px, 305px 252px, 336px 352px, 27px 352px);
    background: linear-gradient(90deg, #b0674c 0%, #c98a6e 45%, #8c8f94 62%, #1f5a6e 80%, #d8d4cc 100%);
  }
</style>
</head>
<body>

<section class="postcard postcard--front">
  <div class="hero-photo" role="img" aria-label="Photo of a yellow model house with a dark tiled roof on a desk"></div>
  <svg class="card-shapes" width="560" height="398" viewBox="0 0 560 398" aria-hidden="true">
    <defs>
      <linearGradient id="panelGradient" x1="0" y1="0" x2="1" y2="0">
        <stop offset="0" stop-color="var(--panel-deep)"/>
        <stop offset="1" stop-color="var(--panel-bright)"/>
      </linearGradient>
    </defs>
    <polygon points="0,111 172,111 181,124 0,124" fill="var(--pale-blue)"/>
    <polygon points="457,71 560,71 560,87 445,87" fill="var(--sky)"/>
    <polygon points="206,124 222,124 351,335 335,335" fill="var(--pale-blue)"/>
    <polygon points="0,124 206,124 335,335 0,335" fill="url(#panelGradient)"/>
    <line x1="4" y1="318" x2="322" y2="318" stroke="var(--white)" stroke-width="1.2" stroke-dasharray="6 5"/>
  </svg>

  <div class="brand">
    <span class="brand-mark"></span>
    <span class="brand-name">Bramblecrest<br>Works</span>
  </div>
  <div class="license">#2839165</div>

  <h1 class="tagline">Ensuring the Safety<br>and Security</h1>

  <p class="hero-copy">
    <span class="light">We are a</span><br>
    <span class="strong">Residential foundation</span><br>
    <span class="strong">inspection &amp; repair</span><br>
    <span class="light">company here in</span><br>
    <span class="city">Los Angeles</span>
  </p>

  <div class="phone">323-555-0148</div>
  <div class="phone-note">For more details, Please contact us</div>
  <div class="email">
    <svg width="22" height="18" viewBox="0 0 22 18" aria-hidden="true">
      <rect x="1" y="3" width="20" height="14" fill="none" stroke="var(--red)" stroke-width="1.3"/>
      <polyline points="1,3 11,11 21,3" fill="none" stroke="var(--red)" stroke-width="1.3"/>
    </svg>
    <span>info@bramblecrestworks.com</span>
  </div>
</section>

<section class="postcard postcard--back">
  <svg class="card-shapes" width="560" height="398" viewBox="0 0 560 398" aria-hidden="true">
    <polygon points="270,56 560,56 560,355 365,355" fill="var(--address-gray)"/>
    <polygon points="274,96 282,96 374,355 366,355" fill="var(--address-edge)"/>
    <rect x="458" y="70" width="66" height="71" rx="5" fill="var(--white)" stroke="#555" stroke-width="1"/>
    <line x1="331" y1="208" x2="524" y2="208" stroke="var(--rule)" stroke-width="0.8"/>
    <line x1="341" y1="239" x2="524" y2="239" stroke="var(--rule)" stroke-width="0.8"/>
    <line x1="352" y1="270" x2="524" y2="270" stroke="var(--rule)" stroke-width="0.8"/>
    <line x1="362" y1="302" x2="524" y2="302" stroke="var(--rule)" stroke-width="0.8"/>
    <rect x="0" y="365" width="560" height="33" fill="var(--brand-blue)"/>
    <line x1="0" y1="369" x2="560" y2="369" stroke="var(--white)" stroke-width="1.5" stroke-dasharray="10 4"/>
  </svg>

  <ul class="services">
    <li>FOUNDATION REPAIR</li>
    <li>EARTHQUAKE RETROFITTING</li>
    <li>REINFORCEMENT</li>
  </ul>

  <div class="goal">
    <p>Our primary objective is to empower clients with comprehensive knowledge about foundation issues and earthquake retrofitting.</p>
    <p>By educating them on the potential risks associated with foundation problems and the importance of earthquake retrofitting, we aim to equip homeowners with the necessary information to make informed decisions about safeguarding their properties.</p>
    <p>Highlighting the benefits of having their houses properly bolted not only enhances structural integrity but also provides peace of mind during seismic events, ensuring the safety and security of their homes and loved ones.</p>
  </div>

  <div class="work-photo" role="img" aria-label="Photo of a worker cutting into a brick wall with an angle grinder"></div>
</section>

</body>
</html>
```